Criação de Power Point Slide Mestre para Outros
A empresa queria:
" Nós intermediamos a venda de minérios entre mineradores brasileiros e compradores internacionais. "

```html
<!DOCTYPE html>
<html lang="pt-BR">
<head>
<meta charset="UTF-8">
<title>Slide Mestre – Verantis</title>
<link rel="stylesheet" href="https://fonts.googleapis.com/css2?family=Exo+2:wght@400;600;700&family=Open+Sans:wght@400;600&display=swap">
<style>
  :root {
    --page: #f1f1f2;
    --slide: #ffffff;
    --ink-dark: #1b1b1d;
    --band: #202023;
    --text: #4a4a4d;
    --muted: #8a8a8e;
    --line: #b9b9bd;
    --white: #ffffff;
    --photo-a: #2a241d;
    --photo-b: #6b5339;
    --photo-c: #a58457;
  }
  * { box-sizing: border-box; margin: 0; padding: 0; }
  html, body { width: 1200px; height: 1200px; overflow: hidden; }
  body { background: var(--page); font-family: "Open Sans", sans-serif; position: relative; }

  .slide {
    position: absolute; left: 30px; top: 296px;
    width: 1140px; height: 608px;
    background: var(--slide);
    overflow: hidden;
    box-shadow: 0 2px 10px rgba(0,0,0,.12);
  }
  .slide-shapes { position: absolute; inset: 0; }

  .slide-title {
    position: absolute; left: 52px; top: 80px;
    font-family: "Exo 2", sans-serif; font-weight: 600;
    font-size: 40px; color: var(--white); letter-spacing: .5px;
  }

  .photo-placeholder {
    position: absolute; left: 28px; top: 212px;
    width: 316px; height: 300px;
    border: 2px solid var(--line); border-radius: 22px;
    background: var(--white);
    display: flex; align-items: center; justify-content: center;
  }

  .subtitle {
    position: absolute; left: 356px; top: 208px; width: 340px;
    font-family: "Exo 2", sans-serif; font-size: 21px; color: var(--muted);
    padding-bottom: 6px; border-bottom: 1px solid var(--line);
  }

  .body-copy {
    position: absolute; left: 356px; top: 262px; width: 350px;
    font-size: 10.5px; line-height: 14.5px; color: var(--text); text-align: justify;
  }

  .footer-copy {
    position: absolute; left: 36px; top: 540px; width: 740px;
    font-size: 9.5px; line-height: 13px; color: #d6d6d8;
  }

  .brand {
    position: absolute; left: 858px; top: 470px; width: 260px; text-align: center;
  }
  .brand-mark { width: 22px; height: 22px; background: var(--ink-dark); margin: 0 auto 10px; }
  .brand-name {
    font-family: "Exo 2", sans-serif; font-weight: 700; font-size: 42px;
    color: var(--ink-dark); letter-spacing: 1px; line-height: 1;
  }
  .brand-tagline {
    font-family: "Exo 2", sans-serif; font-weight: 600; font-size: 10.5px;
    color: #5a2a2a; margin-top: 4px; letter-spacing: .3px;
  }
</style>
</head>
<body>
  <main class="slide">
    <svg class="slide-shapes" width="1140" height="608" viewBox="0 0 1140 608">
      <defs>
        <linearGradient id="harborGradient" x1="0" y1="0" x2="1" y2="1">
          <stop offset="0" stop-color="#151517"/>
          <stop offset=".55" stop-color="var(--photo-a)"/>
          <stop offset="1" stop-color="var(--photo-b)"/>
        </linearGradient>
        <linearGradient id="miningGradient" x1="0" y1="0" x2="1" y2="1">
          <stop offset="0" stop-color="var(--photo-b)"/>
          <stop offset=".5" stop-color="var(--photo-c)"/>
          <stop offset="1" stop-color="var(--photo-a)"/>
        </linearGradient>
      </defs>

      <rect class="header-photo" x="0" y="0" width="860" height="193" fill="url(#harborGradient)"
            role="img" aria-label="Foto de porto com navios e contêineres de carga"/>
      <polygon class="header-light" points="740,0 1140,0 1140,395 980,395" fill="#e4e4e6"/>
      <polygon class="mining-photo" points="790,0 1140,0 1140,330 1010,395 860,160" fill="url(#miningGradient)"
               role="img" aria-label="Fotos de mineração e transporte de minério"/>

      <polygon class="footer-band" points="0,528 850,528 820,584 0,584" fill="var(--band)"/>
      <rect class="footer-line" x="0" y="596" width="1140" height="12" fill="var(--ink-dark)"/>
    </svg>

    <h1 class="slide-title">Título Slide</h1>

    <div class="photo-placeholder">
      <svg width="74" height="60" viewBox="0 0 74 60" aria-label="Ícone de câmera" role="img">
        <path d="M6 14h14l6-8h22l6 8h14a4 4 0 0 1 4 4v34a4 4 0 0 1-4 4H6a4 4 0 0 1-4-4V18a4 4 0 0 1 4-4z"
              fill="none" stroke="var(--ink-dark)" stroke-width="4" stroke-linejoin="round"/>
        <circle cx="37" cy="34" r="12" fill="none" stroke="var(--ink-dark)" stroke-width="4"/>
        <rect x="9" y="19" width="8" height="4" fill="var(--ink-dark)"/>
      </svg>
    </div>

    <h2 class="subtitle">Subtitulo Apresentação</h2>

    <p class="body-copy">Lorem ipsum dolor sit amet, consectetur adipiscing elit. Quisque feugiat, nisi id hendrerit bibendum, tellus erat rhoncus massa, ut blandit nisi velit et lectus. Nunc eu vestibulum mi. Donec nisl nisi, bibendum sit amet facilisis sit amet, pharetra eget risus. Donec volutpat lectus sit amet pellentesque blandit. Vestibulum sed dolor luctus, hendrerit urna non, elementum purus. Aliquam aliquet, lacus nec volutpat condimentum, purus enim pulvinar turpis, vel semper lacus est a neque. Suspendisse potenti. Sed nec massa non tortor pharetra posuere tincidunt eget metus. Fusce rhoncus mi commodo leo tincidunt auctor. Morbi vel augue nec odio semper semper.</p>

    <p class="footer-copy">Lorem ipsum dolor sit amet, consectetur adipiscing elit. Quisque feugiat, nisi id hendrerit bibendum, tellus erat rhoncus massa, ut blandit nisi velit et lectus. Nunc eu vestibulum mi. Donec nisl nisi, bibendum sit amet facilisis sit amet, pharetra eget risus. Donec volutpat lectus sit amet pellentesque blandit.</p>

    <div class="brand">
      <div class="brand-mark"></div>
      <div class="brand-name">VERANTIS</div>
      <div class="brand-tagline">CONSULTORIA EM IMPORTAÇÃO E EXPORTAÇÃO</div>
    </div>
  </main>
</body>
</html>
```